Brennock transport business cards

Front of card, Looking for my logo on one side of the card

Back of card,
Brennock Transport Maintenance
Onsite Cars, Trucks & trailer maintenance and repairs
Gary Brennock
0452918406
Brennocktm@vexmail.test

```html
<!DOCTYPE html>
<html lang="en">
<head>
<meta charset="utf-8">
<title>Brennock Transport Maintenance – Business Cards</title>
<link href="https://fonts.googleapis.com/css2?family=Oswald:wght@500;600&family=Montserrat:wght@400;600&display=swap" rel="stylesheet">
<style>
  :root {
    --page-bg: #3a3a3c;
    --card-dark: #1c1c1d;
    --card-white: #ffffff;
    --brand-blue: #1670c9;
    --ink-black: #111111;
    --text-white: #f4f4f4;
  }
  * { box-sizing: border-box; margin: 0; padding: 0; }
  html, body {
    width: 1200px; height: 1200px; overflow: hidden;
    background: var(--page-bg);
  }
  .sheet {
    width: 1200px; height: 1200px;
    display: flex; flex-direction: column; align-items: center; justify-content: center;
    gap: 60px;
  }
  .card {
    position: relative;
    width: 860px; height: 491px;
    border-radius: 34px;
    overflow: hidden;
    border-bottom: 4px solid var(--brand-blue);
    background: var(--card-dark);
  }

  /* ---------- contact side ---------- */
  .card-contact .top-panel {
    position: absolute; left: 0; top: 0; width: 100%; height: 210px;
    background: var(--card-white);
    display: flex; align-items: center; justify-content: center;
  }
  .card-contact .service-band {
    position: absolute; left: 0; top: 210px; width: 100%; height: 46px;
    background: var(--brand-blue);
    display: flex; align-items: center; justify-content: center;
    font-family: 'Oswald', sans-serif; font-weight: 500;
    font-size: 27px; letter-spacing: 0.5px; text-transform: uppercase;
    color: var(--text-white);
  }
  .contact-block {
    position: absolute; left: 0; top: 268px; width: 100%;
    display: flex; flex-direction: column; align-items: center;
    font-family: 'Montserrat', sans-serif; color: var(--text-white);
  }
  .contact-name {
    font-weight: 600; font-size: 40px; letter-spacing: 6px;
    text-transform: uppercase; color: var(--brand-blue);
    line-height: 1.1;
  }
  .contact-role {
    font-size: 24px; letter-spacing: 3px; text-transform: uppercase;
    margin-top: 2px; margin-left: 150px;
  }
  .contact-line {
    display: flex; align-items: center; gap: 12px;
    font-size: 30px; margin-top: 10px; letter-spacing: 1px;
  }
  .contact-line svg { width: 34px; height: 34px; fill: var(--brand-blue); flex: none; }

  /* ---------- wordmark ---------- */
  .wordmark {
    display: flex; align-items: center; gap: 18px;
  }
  .wordmark-square {
    width: 34px; height: 34px; background: var(--brand-blue); flex: none;
  }
  .wordmark-name {
    font-family: 'Oswald', sans-serif; font-weight: 600;
    font-size: 48px; text-transform: uppercase; letter-spacing: 1px;
    line-height: 1;
  }
  .card-contact .wordmark-name { color: var(--ink-black); }

  /* ---------- logo side ---------- */
  .card-logo {
    display: flex; align-items: center; justify-content: center;
  }
  .card-logo .wordmark-name { color: var(--text-white); font-size: 54px; }
</style>
</head>
<body>
<main class="sheet">

  <section class="card card-contact" aria-label="Contact side">
    <div class="top-panel">
      <div class="wordmark">
        <span class="wordmark-square"></span>
        <span class="wordmark-name">Brennock Transport Maintenance</span>
      </div>
    </div>
    <div class="service-band">Onsite cars, trucks &amp; trailer maintenance and repairs</div>
    <div class="contact-block">
      <p class="contact-name">Gary Brennock</p>
      <p class="contact-role">Owner</p>
      <p class="contact-line">
        <svg viewBox="0 0 24 24" aria-hidden="true"><path d="M6.6 10.8a15.1 15.1 0 0 0 6.6 6.6l2.2-2.2a1 1 0 0 1 1-.25 11.4 11.4 0 0 0 3.6.57 1 1 0 0 1 1 1V20a1 1 0 0 1-1 1A17 17 0 0 1 3 4a1 1 0 0 1 1-1h3.5a1 1 0 0 1 1 1c0 1.25.2 2.45.57 3.57a1 1 0 0 1-.25 1z"/></svg>
        0452918406
      </p>
      <p class="contact-line">
        <svg viewBox="0 0 24 24" aria-hidden="true"><path d="M2 5h20v14H2z" fill="none"/><path d="M2 5h20L12 13z"/><path d="M2 7l10 8 10-8v12H2z"/></svg>
        Brennocktm@vexmail.test
      </p>
    </div>
  </section>

  <section class="card card-logo" aria-label="Logo side">
    <div class="wordmark">
      <span class="wordmark-square"></span>
      <span class="wordmark-name">Brennock Transport Maintenance</span>
    </div>
  </section>

</main>
</body>
</html>
```